Page Template for Quillfern Supply

We are Quillfern Supply, a UK based reseller of Computer Memory, Equipment, Peripherals, Software and Services with a particular focus on Memory and Storage to businesses.

Our succesful ecommerce site at http://www.quillfern-supply.co.uk is now due a refresh. We are looking for a designer to produce a quality page template we can use throughout the site.

We will be using code from our corporate buying system http://k7.qfsupply.me.uk/ and a test version of the system is online at http://test.quillfernsupply.co.uk

We are keen for a "full-width" design - ie one that will stretch with the width of the user's monitor with a minimum width of 950px. It's also important that we can maintain our standards compliance. We are concerned with the colour scheme and layout of the page and the look of the buttons, bars, menus and peripheral elements etc. rather than any content. Please bear in mind that we are a British company and the layout must reflect design trends here rather than in the USA.

Layout should be suitable for product pages (eg. http://k7.qfsupply.me.uk/k7/product.php?id=5830914 ), memory pages (eg. http://k7.qfsupply.me.uk/k7/showMachine.php?machineid=602915 / http://www.brindlepart.co.uk/showMachine.php?machineid=602915 / http://www.quillfern-supply.co.uk/M-Veltrix-Orbdesk (mid+2010)-3.06GHz+Zenn+v3 21.5in-.html ) and content pages (eg http://www.quillfern-supply.co.uk/index.aspx?pageid=5 )

Might also be worth having a look at our other site at www.brindlepart.co.uk

Competitors' sites worth looking at:

www.harlowbyte.co.uk
www.tiwk.com
www.gradelinktrade.co.uk
www.foraxel.co.uk
www.sirplinth.co.uk

Reason: We're getting some great ideas through but we're well aware that quite a few designers are still at work either designing or perfecting designs. We're confident that with another few days of work, we'll be able to make an award.

Good morning, Designers,

Time is running out to participate in this contest, but there is still your opportunity to submit a design and walk away with the prize. Please remember the prize is in £ not $ - £225 is $370 US.

We've had some fantastic designs already, but it is still more than possible that a new designer could win. It is also our intention to award the participation payments to the designers who have put in the most effort, so it's well worth getting on board.

If you have questions please don't hesitate to send us a message.

Best regards,

Quillfern Supply

Target Market(s)

Business IT buyers in corporates and government departments

Industry/Entity Type

Computer

Requirements
Must have
• Must include:
a) large page content area
b) logo in top left
c) search box
d) QuickPeg code box
e) Shopping cart
f) full category menu per http://k7.qfsupply.me.uk
Should not have
• DO NOT ALTER OUR LOGO! This is non negotiable. Please also do not change the key corporate colour of #333399

```html
<!DOCTYPE html>
<html lang="en">
<head>
<meta charset="utf-8">
<title>Quillfern Supply – Home</title>
<link rel="stylesheet" href="https://fonts.googleapis.com/css2?family=Noto+Sans:wght@400;700&family=Archivo+Black&family=Tinos:wght@700&display=swap">
<style>
:root{
  --brand:#333399;
  --brand-dark:#2a2a80;
  --ink:#333333;
  --muted:#7a7a7a;
  --rule:#cfcfcf;
  --panel:#e6e6e6;
  --banner:#111111;
  --white:#ffffff;
  --feed:#f29a1e;
}
*{box-sizing:border-box;margin:0;padding:0}
html,body{width:1200px;height:998px;overflow:hidden;background:var(--white)}
body{font-family:"Noto Sans",Tahoma,sans-serif;color:var(--ink)}
.page{position:relative;width:1300px;height:1081px;transform:scale(.9231);transform-origin:0 0}
.abs{position:absolute}

/* header */
.logo{left:180px;top:30px;display:flex;align-items:center;gap:8px}
.logo-mark{width:22px;height:22px;background:var(--brand)}
.logo-name{font-size:22px;font-weight:700;color:var(--brand);line-height:1}
.phone{left:181px;top:114px;font-family:Tinos,serif;font-weight:700;font-size:17px;color:#111;letter-spacing:.5px}
.toplinks{right:202px;top:50px;font-size:12px;color:var(--brand);display:flex;gap:10px}
.toplinks span.sep{color:var(--brand)}
.feed{left:1108px;top:47px;width:22px;height:22px;background:var(--feed);border-radius:3px}
.cart{right:170px;top:70px;display:flex;align-items:center;gap:6px;font-size:12px;color:var(--brand)}
.searchbar{left:737px;top:101px;width:393px;height:43px;background:var(--brand);border-radius:6px 6px 0 0;display:flex;align-items:center;padding:0 10px;font-size:12px;color:var(--white)}
.searchbar input{height:20px;border:0;background:var(--white)}
.btn-go{background:#5d5db3;color:var(--white);font-size:11px;height:20px;padding:0 3px;line-height:20px}
.btn-search{background:#5d5db3;color:var(--white);font-size:11px;height:20px;padding:0 8px;line-height:20px}

/* nav */
.mainnav{left:180px;top:144px;width:950px;height:36px;background:var(--brand);display:flex;font-size:12px;color:var(--white)}
.mainnav li{list-style:none;padding:0 13px 0 15px;line-height:36px;border-right:1px solid #4b4bab}

/* banner */
.banner{left:180px;top:180px;width:950px;height:284px;background:var(--banner);overflow:hidden}
.banner-art{position:absolute;left:490px;top:0;width:460px;height:284px;background:radial-gradient(ellipse at 60% 50%,#1d5f9a 0%,#0d2c4a 45%,#111 75%)}
.banner-kicker{position:absolute;left:56px;top:68px;font-size:23px;color:var(--white)}
.banner-title{position:absolute;left:96px;top:105px;font-family:"Archivo Black",sans-serif;font-size:31px;line-height:37px;color:var(--white);letter-spacing:.5px}
.banner-sub{position:absolute;left:95px;top:176px;font-size:17px;color:var(--white)}
.dots{position:absolute;left:19px;top:258px;display:flex;gap:5px}
.dots i{width:10px;height:10px;border-radius:50%;background:#777}
.dots i.on{background:var(--white)}

/* sidebar */
.sidebar{left:180px;top:478px;width:235px}
.sidebar h3{font-size:14px;font-weight:700;padding-bottom:9px;border-bottom:1px solid #555;color:var(--ink)}
.sidebar li{list-style:none;height:36px;line-height:42px;border-bottom:1px solid #ddd;font-size:12px;letter-spacing:.6px;padding-left:23px;position:relative;color:#444}
.sidebar li::before{content:"";position:absolute;left:1px;top:19px;border-left:3px solid var(--brand);border-top:2px solid transparent;border-bottom:2px solid transparent}

/* boxes */
.box{border:1px solid var(--rule)}
.carousel{left:421px;top:477px;width:710px;height:189px}
.arrow{position:absolute;top:78px;color:#ccc;font-size:30px}
.cat{position:absolute;text-align:center;font-size:12px;color:var(--ink)}
.cat .pic{margin:0 auto 8px}
.popular{left:421px;top:671px;width:710px;height:237px}
.popular h2{position:absolute;left:17px;top:6px;font-size:15px;font-weight:700;color:#999}
.prod{position:absolute;top:38px}
.prod .frame{width:167px;height:119px;border:1px solid #ddd;display:flex;align-items:center;justify-content:center}
.prod .pname{margin-top:19px;font-size:12px;color:var(--muted)}
.prod .price{font-size:24px;color:var(--muted);margin-top:0}
.addcart{position:absolute;background:var(--brand);color:var(--white);font-size:12px;padding:0 7px;height:28px;line-height:28px;top:151px}

.partners{left:180px;top:915px;width:951px;height:96px}
.brand{position:absolute;top:38px;font-size:17px;font-weight:700;color:var(--brand)}
.paybox{position:absolute;left:712px;top:5px;width:232px;height:84px;background:var(--panel)}
.paybox .card{position:absolute;top:0;width:36px;height:22px;background:#bbb;border-radius:2px}

/* footer */
.footer{left:180px;top:1023px;width:951px;height:36px;background:var(--brand);color:var(--white);font-size:12px;display:flex;align-items:center;justify-content:space-between;padding:0 16px}
.footer nav{display:flex;gap:10px}
</style>
</head>
<body>
<div class="page">

  <header>
    <div class="abs logo"><span class="logo-mark"></span><span class="logo-name">Quillfern Supply</span></div>
    <div class="abs phone">020 7946 0321</div>

    <nav class="abs toplinks">
      <span>Login</span><span class="sep">|</span><span>Regiter</span><span class="sep">|</span><span>FAQ</span><span class="sep">|</span><span>About Us</span><span class="sep">|</span><span>Contact Us</span>
    </nav>
    <span class="abs feed" role="img" aria-label="News feed"></span>

    <div class="abs cart">
      <svg width="28" height="24" viewBox="0 0 28 24" aria-hidden="true">
        <path d="M1 3h5l3 12h13l3-9H8" fill="none" stroke="#555" stroke-width="2"/>
        <circle cx="11" cy="20" r="2" fill="#555"/><circle cx="21" cy="20" r="2" fill="#555"/>
        <circle cx="13" cy="5" r="4" fill="#3aa33a"/><path d="M13 3v4M11 5h4" stroke="#fff" stroke-width="1.5"/>
      </svg>
      <span>Shopping cart is empty</span>
    </div>

    <form class="abs searchbar">
      <span>QuickPeg:</span>
      <input style="width:93px;margin-left:6px" aria-label="QuickPeg code">
      <span class="btn-go">GO</span>
      <span style="margin-left:10px">Seach:</span>
      <input style="width:100px;margin-left:6px" aria-label="Search">
      <span class="btn-search" style="margin-left:4px">Search</span>
    </form>
  </header>

  <ul class="abs mainnav">
    <li>Home</li><li>Memory</li><li>Audio Visual</li><li>Printers</li><li>PC &amp; Laptops</li><li>Networking</li><li>Components</li><li>Storage</li><li>Software</li>
  </ul>

  <section class="abs banner">
    <div class="banner-art" role="img" aria-label="Photo of a blue and black motherboard with feature callouts"></div>
    <div class="banner-kicker">K4X70 Series Motherboards</div>
    <div class="banner-title">YOUR DREAM<br>X70 MOTHERBOARD</div>
    <div class="banner-sub">Smarter, Faster, and more Efficient</div>
    <div class="dots"><i></i><i></i><i></i><i class="on"></i><i></i></div>
  </section>

  <aside class="abs sidebar">
    <h3>Shop buy Categories</h3>
    <ul>
      <li>Memory</li><li>AV</li><li>Cables</li><li>Components</li><li>Computing</li><li>Media</li><li>Networking</li><li>Power</li><li>Printing</li><li>Software</li><li>Storage</li>
    </ul>
  </aside>

  <section class="abs box carousel">
    <span class="arrow" style="left:14px">‹</span>
    <span class="arrow" style="right:12px">›</span>
    <div class="cat" style="left:50px;top:17px;width:102px">
      <div class="pic" role="img" aria-label="Photo of a desktop tower" style="width:70px;height:126px;background:linear-gradient(#3a3a3a,#111)"></div>Desktops</div>
    <div class="cat" style="left:190px;top:19px;width:167px">
      <div style="border:1px solid #ddd;height:133px;padding-top:14px"><div class="pic" role="img" aria-label="Photo of a laptop" style="width:130px;height:104px;background:linear-gradient(#2a6fd0,#bfc4c8)"></div></div>
      <div style="margin-top:-23px;margin-top:4px">Notebooks</div></div>
    <div class="cat" style="left:378px;top:19px;width:166px">
      <div class="pic" role="img" aria-label="Photo of an inkjet printer with photo prints" style="width:150px;height:126px;background:linear-gradient(#eee,#333)"></div><div style="margin-top:12px">Printers</div></div>
    <div class="cat" style="left:562px;top:37px;width:120px">
      <div class="pic" role="img" aria-label="Photo of a silver camcorder" style="width:110px;height:100px;background:linear-gradient(#ccc,#777)"></div><div style="margin-top:20px">Cameras</div></div>
  </section>

  <section class="abs box popular">
    <h2>Popular products:</h2>
    <div class="prod" style="left:35px">
      <div class="frame"><div role="img" aria-label="Photo of a flat screen television" style="width:110px;height:86px;background:linear-gradient(135deg,#222,#7a3fb0,#e07030)"></div></div>
      <div class="pname" style="margin-left:-19px">Lorem ipsum dolor</div>
      <div class="price" style="margin-left:-19px">250.00</div>
    </div>
    <span class="addcart" style="left:128px;top:189px">Add to Cart</span>

    <div class="prod" style="left:290px">
      <div class="frame" style="border:0"><div role="img" aria-label="Photo of a widescreen monitor" style="width:116px;height:80px;background:linear-gradient(#222,#6b4a3a,#111)"></div></div>
      <div class="pname" style="margin-left:-29px">Lorem ipsum dolor</div>
      <div class="price" style="margin-left:-29px">250.00</div>
    </div>
    <span class="addcart" style="left:373px;top:189px">Add to Cart</span>

    <div class="prod" style="left:486px">
      <div class="frame" style="border:0"><div role="img" aria-label="Photo of a media player with earphones" style="width:140px;height:44px;background:linear-gradient(#ddd,#333)"></div></div>
      <div class="pname">Lorem ipsum dolor</div>
      <div class="price">250.00</div>
    </div>
    <span class="addcart" style="left:598px;top:189px">Add to Cart</span>
  </section>

  <section class="abs box partners">
    <span class="brand" style="left:22px">Korvane</span>
    <span class="brand" style="left:125px">Pelidor</span>
    <span class="brand" style="left:225px">Tamsk</span>
    <span class="brand" style="left:322px">Velloro</span>
    <span class="brand" style="left:427px">Ardent</span>
    <span class="brand" style="left:518px">Sumvik</span>
    <span class="brand" style="left:610px">Zerolin</span>
    <div class="paybox" role="img" aria-label="Accepted payment methods">
      <div style="position:absolute;left:22px;top:22px;width:190px;height:46px;border:1px solid #9a9ab8;background:#fff">
        <span class="card" style="left:8px;top:12px"></span>
        <span class="card" style="left:52px;top:12px"></span>
        <span class="card" style="left:96px;top:12px"></span>
        <span class="card" style="left:140px;top:12px"></span>
      </div>
    </div>
  </section>

  <footer class="abs footer">
    <nav><span>Home</span><span>|</span><span>Terms &amp; Conditions</span><span>|</span><span>Privacy Policy</span><span>|</span><span>About</span><span>|</span><span>Contact</span></nav>
    <span>©2011 Powered by Quillfern Supply Ltd. All rights reserved</span>
  </footer>

</div>
</body>
</html>
```